Willowmere Counseling (Endure - Mend - Flourish) - Double Sided Business Card

I would like a 2-sided business card. Front: Matte Black or Navy with Logo & Tagline. Back: Name, Address, Phone Number, Email, & Website (maybe would like to include a small map pin-pointing location); Prefer front to be a gold/silver foil (iridescent); Back prefer white or light colored background with lettering that is easy to read and simple

Target Market(s)

Individuals & Couples (13 y.o. - ALL Adults); High end clientele

Industry/Entity Type

Licensed Professional Counselor (Mental Health)

Contact Information for Business Card

Name: Willowmere Counseling; Tagline: Endure - Mend - Flourish; Address: 3870 N. Garrick Ave., Suite 214, Fort Worth, TX 76132; Phone: (214) 555-0187; Website: www.WillowmereCounseling.example

Font styles to use
Serif

Requirements
Must have
• Logo on Front (Large) prefer gold/silver foil on a matte dark color (i.e. black, navy, etc.); Back of Card: All other relevant information

```html
<!DOCTYPE html>
<html lang="en">
<head>
<meta charset="utf-8">
<title>Willowmere Counseling – Business Card</title>
<link rel="stylesheet" href="https://fonts.googleapis.com/css2?family=Cinzel:wght@500&family=Poppins:wght@400;700&display=swap">
<style>
  :root {
    --backdrop: #2e2724;
    --card: #141414;
    --card-edge: #0c0c0c;
    --silver: #b9b9b9;
    --gold: #e6c15a;
    --gold-line: #b8993c;
    --muted: #9c9c9c;
  }
  * { box-sizing: border-box; margin: 0; padding: 0; }
  html, body { width: 1200px; height: 716px; overflow: hidden; }
  body {
    background: var(--backdrop);
    display: flex;
    align-items: center;
    justify-content: center;
    gap: 40px;
    font-family: "Poppins", sans-serif;
  }
  .card {
    position: relative;
    width: 520px;
    height: 298px;
    background: var(--card);
    border: 1px solid var(--card-edge);
    box-shadow: 0 14px 30px rgba(0,0,0,.45);
    overflow: hidden;
  }
  .wordmark {
    display: flex;
    flex-direction: column;
    align-items: center;
    font-family: "Cinzel", serif;
    font-weight: 500;
  }
  .wordmark__row { display: flex; align-items: center; gap: 12px; }
  .wordmark__dot { width: 14px; height: 14px; border-radius: 50%; }
  .wordmark__name { font-size: 30px; letter-spacing: 1px; line-height: 1.1; }
  .wordmark__tagline { font-size: 10.5px; letter-spacing: 1.5px; margin-top: 6px; }

  /* Front */
  .card--front { display: flex; align-items: center; justify-content: center; }
  .card--front .wordmark { color: var(--silver); }
  .card--front .wordmark__dot { background: var(--silver); }

  /* Back */
  .card--back .wordmark {
    position: absolute; left: 60px; top: 46px; width: 250px;
    color: var(--gold);
  }
  .card--back .wordmark__name { font-size: 21px; }
  .card--back .wordmark__tagline { font-size: 8px; letter-spacing: 1px; }
  .card--back .wordmark__dot { width: 10px; height: 10px; background: var(--gold); }
  .divider {
    position: absolute; left: 28px; right: 28px; top: 142px;
    height: 1px; background: var(--gold-line);
  }
  .contact {
    position: absolute; left: 30px; top: 158px;
    list-style: none; font-size: 11px; color: var(--muted);
  }
  .contact li { display: flex; align-items: center; gap: 8px; line-height: 19px; }
  .contact svg { width: 10px; height: 10px; fill: var(--gold); flex: none; }
  .contact .contact__web { color: var(--gold); }
  .person {
    position: absolute; right: 34px; top: 200px; text-align: right;
  }
  .person__name { font-weight: 700; font-size: 15px; letter-spacing: .5px; color: var(--gold); }
  .person__title { font-size: 11px; color: var(--muted); margin-top: 1px; }
  .person__address { font-size: 11px; color: var(--muted); line-height: 16px; margin-top: 10px; }
  .edge-bar {
    position: absolute; right: 16px; top: 204px;
    width: 3px; height: 30px; background: var(--gold);
  }
</style>
</head>
<body>
  <section class="card card--front" aria-label="Card front">
    <div class="wordmark">
      <div class="wordmark__row">
        <span class="wordmark__dot"></span>
        <span class="wordmark__name">Willowmere Counseling</span>
      </div>
      <span class="wordmark__tagline">Endure - Mend - Flourish</span>
    </div>
  </section>

  <section class="card card--back" aria-label="Card back">
    <div class="wordmark">
      <div class="wordmark__row">
        <span class="wordmark__dot"></span>
        <span class="wordmark__name">Willowmere Counseling</span>
      </div>
      <span class="wordmark__tagline">Endure - Mend - Flourish</span>
    </div>
    <div class="divider"></div>
    <ul class="contact">
      <li>
        <svg viewBox="0 0 24 24"><path d="M6.6 10.8a15 15 0 0 0 6.6 6.6l2.2-2.2a1 1 0 0 1 1-.25 11.4 11.4 0 0 0 3.6.57 1 1 0 0 1 1 1V20a1 1 0 0 1-1 1A17 17 0 0 1 3 4a1 1 0 0 1 1-1h3.5a1 1 0 0 1 1 1c0 1.25.2 2.45.57 3.57a1 1 0 0 1-.25 1z"/></svg>
        (214) 555-0187
      </li>
      <li>
        <svg viewBox="0 0 24 24"><path d="M2 5h20v14H2z M2 5l10 8 10-8" /></svg>
        info@WillowmereCounseling.example
      </li>
      <li class="contact__web">
        <svg viewBox="0 0 24 24"><circle cx="12" cy="12" r="10"/></svg>
        www.WillowmereCounseling.example
      </li>
    </ul>
    <div class="person">
      <div class="person__name">DANIEL ASHFORD</div>
      <div class="person__title">CEO &amp; President</div>
      <div class="person__address">3870 N. Garrick Ave., Suite 214<br>Fort Worth, TX 76132</div>
    </div>
    <div class="edge-bar"></div>
  </section>
</body>
</html>
```